Ferrowave.com website design

I need a basic website for www.ferrowave.com. Ferro Wave has been hosting websites since 2002 via partnership arrangement with Stackhollow.com and Namequarry.com. We do not do any design, only hosting for small companies and nonprofits. We are referring people to PixelGuild and others to get their websites developed. Our website and pricing does not change often, but I need to be able to easily update the pricing and contact page.

Target Market(s)

Small company and non profit organizations

Industry/Entity Type

Utility

Coding

Coded - Design and coding required

Number of Pages Required

5+ page

Colors

Designer to choose colors to be used in the design.

Requirements
Must have
• Wordsmith format for easy content management. The logo attached. Contact us page with the following: Phone and fax are the same number: 888.514.2973. Email address is myferrowave@mailnest.example. Mailing address is 4819 E. Tolliver Bend #317, Ashcombe, AR 72508.
Nice to have
• Some kind of badge or tag line on the home page that celebrates our 15th year of hosting without a single hosting without any downtime. We are are 15 year partners with Stackhollow.com and Namequarry.com. Website Design tab needs to reference PixelGuild or others for all their website design needs. We provide no design or updating services. We will provide the developers FTP access to our dedicated Linux server. We do not provide email services other than redirects to their proprietary email or gmail, yahoo, etc. Needs a services and pricing tab. We provide domain registration services via our partnership with Namequarry.com. We will want a way for them to submit a suggested domain name for us to verify if available. I might be able to get a link from Namequarry.com to our account for you to include on that tab REGISTER DOMAIN. The tab buttons can be: WHO WE ARE, WHAT WE DO, WHEN YOU NEED US, WHERE TO REACH US. Maybe consider making the WHO, WHAT, WHEN and WHERE a dark blue color the rest of the text different color just so they stand out
Should not have
• A lot of animation that takes a long time to open. Clean and simple website.

```html
<!DOCTYPE html>
<html lang="en">
<head>
<meta charset="utf-8">
<title>Ferro Wave — Website Hosting</title>
<link rel="stylesheet" href="https://fonts.googleapis.com/css2?family=Arimo:wght@400;700&display=swap">
<style>
  :root {
    --blue-dark: #0a53a5;
    --blue-light: #3d8ede;
    --button: #3d8ede;
    --ink: #111111;
    --text: #222222;
    --panel: #f0f0f0;
    --rule: #cfcfcf;
    --white: #ffffff;
    --icon: #143a5c;
    --partner-green: #1f7a3c;
    --partner-teal: #1f5e80;
    --partner-red: #c8102e;
  }
  * { box-sizing: border-box; margin: 0; padding: 0; }
  html, body { width: 1200px; height: 2441px; overflow: hidden; }
  body { font-family: "Arimo", Arial, sans-serif; color: var(--text); background: var(--white); }
  a { color: inherit; text-decoration: none; }

  .contact-line { display: flex; align-items: center; gap: 10px; font-size: 15px; color: var(--white); white-space: nowrap; }
  .contact-line svg { width: 16px; height: 16px; flex: none; }
  .contact-line .gap { width: 14px; }

  .topbar {
    height: 51px; background: var(--blue-light);
    display: flex; justify-content: space-between; align-items: center;
    padding: 0 22px;
  }
  .topbar .address { font-size: 15px; color: var(--white); white-space: nowrap; }

  .masthead {
    height: 155px; background: var(--blue-dark);
    display: flex; align-items: center; padding: 0 26px;
  }
  .brand { display: flex; align-items: center; gap: 12px; width: 298px; }
  .brand-mark { width: 30px; height: 30px; background: var(--white); flex: none; }
  .brand-name { font-size: 30px; font-weight: 700; color: var(--white); letter-spacing: 0.5px; text-transform: uppercase; white-space: nowrap; }
  .main-nav { display: flex; }
  .main-nav a { font-size: 18px; color: var(--white); margin-right: 54px; text-transform: uppercase; }

  .hero {
    height: 504px;
    background: linear-gradient(100deg, #5a3a2e 0%, #8b6a55 30%, #c9bfb3 55%, #e9e6df 75%, #9aa58a 100%);
  }

  .intro {
    height: 195px; display: flex; align-items: center;
    padding: 0 22px; border-bottom: 2px solid var(--rule);
  }
  .intro h1 { width: 302px; font-size: 30px; line-height: 37px; font-weight: 700; color: var(--ink); }
  .intro p { width: 560px; font-size: 17px; line-height: 27px; color: var(--text); }
  .btn {
    display: inline-flex; align-items: center; justify-content: center;
    background: var(--button); color: var(--white);
    font-size: 18px; text-transform: uppercase;
  }
  .intro .btn { width: 201px; height: 59px; margin-left: 71px; font-size: 17px; }

  .offer {
    height: 832px; background: var(--panel);
    border-bottom: 2px solid var(--rule);
    padding-top: 138px; text-align: center;
  }
  .offer h2 { font-size: 40px; font-weight: 700; color: var(--ink); }
  .offer .lead { width: 915px; margin: 42px auto 0; font-size: 19.5px; line-height: 31px; color: var(--ink); }
  .services { display: flex; justify-content: space-between; width: 1208px; margin: 70px auto 0; }
  .service { width: 400px; display: flex; flex-direction: column; align-items: center; }
  .service-icon { width: 52px; height: 52px; }
  .service h3 { margin-top: 22px; font-size: 25px; font-weight: 700; color: var(--ink); }
  .service p { margin-top: 22px; width: 345px; font-size: 16.5px; line-height: 22px; color: var(--ink); }
  .service .btn { margin-top: 24px; width: 201px; height: 57px; }

  .partners { height: 464px; text-align: center; padding-top: 100px; }
  .partners h2 { font-size: 38px; font-weight: 700; color: var(--ink); }
  .partners .sub { margin-top: 4px; font-size: 18px; color: var(--ink); }
  .partner-row { display: flex; justify-content: space-between; margin-top: 96px; }
  .partner { width: 400px; display: flex; justify-content: center; align-items: center; gap: 10px; font-size: 32px; font-weight: 700; }
  .partner-stack { color: var(--ink); }
  .partner-stack .dot { width: 26px; height: 26px; border-radius: 50%; background: var(--partner-red); }
  .partner-name { color: var(--partner-green); }
  .partner-pixel { color: var(--partner-teal); }
  .partner-pixel .dot { width: 24px; height: 24px; background: var(--partner-teal); }

  .site-footer {
    height: 240px; background: var(--blue-dark);
    position: relative; padding: 80px 22px 0;
  }
  .footer-nav { display: flex; }
  .footer-nav a { font-size: 16.5px; color: var(--white); margin-right: 42px; text-transform: uppercase; }
  .site-footer .contact-line { margin-top: 14px; font-size: 16px; }
  .site-footer .address { margin-top: 13px; font-size: 16px; color: var(--white); }
  .footer-brand {
    position: absolute; right: 22px; top: 78px;
    display: flex; flex-direction: column; align-items: center; gap: 14px;
  }
  .footer-brand .brand-mark { width: 80px; height: 80px; }
  .footer-brand .brand-name { font-size: 17px; letter-spacing: 0.3px; }
</style>
</head>
<body>

<header>
  <div class="topbar">
    <div class="contact-line">
      <svg viewBox="0 0 16 16" aria-hidden="true"><rect x="1" y="3" width="14" height="10" fill="none" stroke="#fff" stroke-width="1.2"/><path d="M1 3l7 6 7-6" fill="none" stroke="#fff" stroke-width="1.2"/></svg>
      <span>myferrowave@mailnest.example</span>
      <span class="gap"></span>
      <svg viewBox="0 0 16 16" aria-hidden="true"><rect x="0" y="0" width="16" height="16" rx="2" fill="#fff"/><path d="M5 3.5l2 2.2-1.2 1.5c.7 1.4 1.7 2.4 3 3l1.5-1.2 2.2 2-1.2 1.7c-3.6-.4-7.2-4-7.6-7.6z" fill="var(--blue-light)"/></svg>
      <span>888.514.2973</span>
    </div>
    <div class="address">4819 E. Tolliver Bend #317, Ashcombe, AR 72508</div>
  </div>
  <div class="masthead">
    <div class="brand">
      <span class="brand-mark"></span>
      <span class="brand-name">Ferro Wave</span>
    </div>
    <nav class="main-nav">
      <a href="#">Home</a>
      <a href="#">About</a>
      <a href="#">Services</a>
      <a href="#">Pricing</a>
      <a href="#">Contact</a>
    </nav>
  </div>
</header>

<main>
  <section class="hero" role="img" aria-label="Photo of a smiling couple at a laptop, one holding a payment card, in a bright home"></section>

  <section class="intro">
    <h1>Hosting Websites Since 2002</h1>
    <p>Et harum quidem rerum facilis est et expedita distinctio. Nam libero tempore, cum soluta nobis est eligendi optio cumque nihil impedit quo minus id quod maxime.</p>
    <a class="btn" href="#">Read More</a>
  </section>

  <section class="offer">
    <h2>What We Offer</h2>
    <p class="lead">Ut enim ad minima veniam, quis nostrum exercitationem ullam corporis suscipit laboriosam, nisi ut aliquid ex ea commodi consequatur? Quis autem vel eum iure reprehenderit qui in ea voluptate velit esse quam nihil molestiae consequatur, vel illum qui dolorem eum fugiat quo voluptas nulla pariatur</p>
    <div class="services">
      <article class="service">
        <svg class="service-icon" viewBox="0 0 52 52" aria-hidden="true"><circle cx="26" cy="26" r="26" fill="var(--icon)"/><rect x="16" y="16" width="20" height="14" rx="1.5" fill="#fff"/><rect x="13" y="32" width="26" height="4" rx="1" fill="#fff"/></svg>
        <h3>Web Site Hosting</h3>
        <p>Sed ut perspiciatis unde omnis iste natus error sit voluptatem accusantium doloremque laudantium.</p>
        <a class="btn" href="#">Read More</a>
      </article>
      <article class="service">
        <svg class="service-icon" viewBox="0 0 52 52" aria-hidden="true"><circle cx="26" cy="26" r="26" fill="var(--icon)"/><rect x="15" y="17" width="18" height="18" rx="2" fill="none" stroke="#fff" stroke-width="2.4"/><path d="M22 30l2-5 11-11 3 3-11 11z" fill="#fff"/></svg>
        <h3>Domain Registration</h3>
        <p>Sed ut perspiciatis unde omnis iste natus error sit voluptatem accusantium doloremque laudantium.</p>
        <a class="btn" href="#">Read More</a>
      </article>
      <article class="service">
        <svg class="service-icon" viewBox="0 0 52 52" aria-hidden="true"><circle cx="26" cy="26" r="26" fill="var(--icon)"/><rect x="15" y="14" width="22" height="7" rx="1.5" fill="#fff"/><rect x="15" y="23" width="22" height="7" rx="1.5" fill="#fff"/><rect x="15" y="32" width="22" height="7" rx="1.5" fill="#fff"/></svg>
        <h3>FTP Access</h3>
        <p>Sed ut perspiciatis unde omnis iste natus error sit voluptatem accusantium doloremque laudantium.</p>
        <a class="btn" href="#">Read More</a>
      </article>
    </div>
  </section>

  <section class="partners">
    <h2>Our Partners</h2>
    <p class="sub">We are 15 years in partners with:</p>
    <div class="partner-row">
      <div class="partner partner-stack"><span class="dot"></span><span>Stackhollow</span></div>
      <div class="partner partner-name"><span>Namequarry.com</span></div>
      <div class="partner partner-pixel"><span class="dot"></span><span>PixelGuild</span></div>
    </div>
  </section>
</main>

<footer class="site-footer">
  <nav class="footer-nav">
    <a href="#">Home</a>
    <a href="#">About</a>
    <a href="#">Services</a>
    <a href="#">Pricing</a>
    <a href="#">Contact</a>
  </nav>
  <div class="contact-line">
    <svg viewBox="0 0 16 16" aria-hidden="true"><rect x="1" y="3" width="14" height="10" fill="none" stroke="#fff" stroke-width="1.2"/><path d="M1 3l7 6 7-6" fill="none" stroke="#fff" stroke-width="1.2"/></svg>
    <span>myferrowave@mailnest.example</span>
    <span class="gap"></span>
    <svg viewBox="0 0 16 16" aria-hidden="true"><rect x="0" y="0" width="16" height="16" rx="2" fill="#fff"/><path d="M5 3.5l2 2.2-1.2 1.5c.7 1.4 1.7 2.4 3 3l1.5-1.2 2.2 2-1.2 1.7c-3.6-.4-7.2-4-7.6-7.6z" fill="var(--blue-dark)"/></svg>
    <span>888.514.2973</span>
  </div>
  <p class="address">4819 E. Tolliver Bend #317, Ashcombe, AR 72508</p>
  <div class="footer-brand">
    <span class="brand-mark"></span>
    <span class="brand-name">Ferro Wave</span>
  </div>
</footer>

</body>
</html>
```